Banner dimension 1767 X 887 for Tovarelo website

Need one banner for our website www.tovarelo.com.au, The dimension of the banner should be 1767 x 887. Attached to this brief are two images that needs to be on that one banner, PLEASE DO NOT SEND SEPARATE BANNERS, both images on the same banner. Thanks

The banner should have the following message on it:

1.) " Take a further 40% off all stock" ( use code: TOVARELO. Ends 31/12/2015)
2.) " Kick back or kick it up a notch this Autumn in the most versatile pique striped polo shirts and Pinafore belt strap denim dress"

Target Market(s)

kids aged 5-12yrs

Requirements
Must have
• very playful

```html
<!DOCTYPE html>
<html lang="en">
<head>
<meta charset="utf-8">
<title>Tovarelo – Autumn Sale Banner</title>
<link rel="stylesheet" href="https://fonts.googleapis.com/css2?family=Archivo+Black&family=Open+Sans:wght@300;400;700;800&display=swap">
<style>
  :root {
    --page: #ffffff;
    --ink: #111111;
    --ink-soft: #3a3a3a;
    --slate: #2f536b;
    --forest: #1f3d2e;
    --white: #ffffff;
    --teal: #2fb3b5;
    --sky: #5a8fd0;
    --blush: #e9b7b8;
    --orange: #f29a1e;
    --amber: #f7b21a;
    --yellow: #ffd21f;
    --lime: #78cf2a;
    --polo: #4f7a5a;
    --shorts: #9fb3c4;
    --tee: #eef0f2;
    --denim: #3f6a8a;
  }
  * { margin: 0; padding: 0; box-sizing: border-box; }
  html, body { width: 1200px; height: 1000px; overflow: hidden; background: var(--page); }
  .banner {
    position: absolute; left: 35px; top: 202px; width: 1135px; height: 568px;
    background: var(--white); overflow: hidden;
    box-shadow: 3px 4px 5px rgba(0,0,0,.55);
    font-family: "Open Sans", Arial, sans-serif;
  }
  .backdrop { position: absolute; inset: 0; width: 100%; height: 100%; }
  .photo { position: absolute; border-radius: 18px; }
  .photo-boy {
    left: 8px; top: 14px; width: 330px; height: 548px;
    background: linear-gradient(180deg, #6b4a3a 0%, var(--polo) 22%, var(--polo) 50%, var(--shorts) 62%, #c79a7c 80%, #2a2a2a 100%);
    opacity: .8;
  }
  .photo-girl {
    left: 858px; top: 0; width: 272px; height: 568px;
    background: linear-gradient(180deg, #3b2a22 0%, var(--tee) 25%, var(--denim) 38%, var(--denim) 82%, #d9a88a 100%);
    opacity: .85;
  }
  .offer-lead, .offer-tail, .deal, .code-band, .headline, .product-tag { position: absolute; }
  .offer-lead, .offer-tail {
    font-family: "Archivo Black", "Arial Black", sans-serif; color: var(--ink-soft);
    font-size: 28px; line-height: 1.3; transform: rotate(-8deg);
  }
  .offer-lead { left: 438px; top: 78px; }
  .offer-lead .indent { padding-left: 6px; }
  .offer-tail { left: 806px; top: 26px; font-size: 26px; }
  .deal {
    left: 570px; top: 8px; height: 150px;
    display: flex; align-items: center; color: var(--slate);
    transform: rotate(-8deg);
  }
  .deal .brace { font-weight: 800; font-size: 140px; line-height: 1; margin: -18px -4px 0; }
  .deal .amount {
    font-family: "Archivo Black", "Arial Black", sans-serif; font-size: 56px;
    line-height: .9; text-align: center; letter-spacing: -1px;
  }
  .code-band {
    left: 258px; top: 158px; width: 632px; height: 46px;
    background: var(--forest); color: var(--white);
    transform: rotate(2.5deg); display: flex; align-items: center;
    padding-left: 10px; font-weight: 800; white-space: nowrap;
  }
  .code-band .code { font-size: 25px; letter-spacing: .5px; }
  .code-band .ends { font-size: 19px; margin-left: 22px; }
  .headline {
    left: 282px; top: 226px; width: 640px;
    font-family: "Archivo Black", "Arial Black", sans-serif; color: var(--ink);
    font-size: 30px; line-height: 1.2; font-weight: 400; transform: rotate(3deg);
    white-space: nowrap;
  }
  .headline .line-two { display: block; padding-left: 12px; }
  .headline .season { font-size: 42px; }
  .product-tag {
    color: var(--white); font-size: 26px; line-height: 1.15;
    padding: 6px 18px 8px; white-space: nowrap;
  }
  .product-tag .light { font-weight: 300; display: block; }
  .product-tag .bold { font-weight: 700; display: block; }
  .tag-polo { left: 327px; top: 320px; width: 390px; background: var(--slate); transform: rotate(3deg); }
  .tag-dress { left: 548px; top: 430px; width: 336px; background: var(--forest); text-align: right; transform: rotate(3deg); }
</style>
</head>
<body>
<main class="banner">
  <svg class="backdrop" viewBox="0 0 1135 568" preserveAspectRatio="none" role="img" aria-label="Soft watercolour wash background in teal, orange, yellow and green">
    <defs>
      <linearGradient id="washCool" x1="0" y1="0" x2="1" y2="1">
        <stop offset="0" stop-color="#2fb3b5"/>
        <stop offset=".5" stop-color="#5a8fd0" stop-opacity=".8"/>
        <stop offset="1" stop-color="#e9b7b8" stop-opacity=".6"/>
      </linearGradient>
      <linearGradient id="washWarm" x1="0" y1="1" x2="1" y2="0">
        <stop offset="0" stop-color="#e8701a"/>
        <stop offset="1" stop-color="#f7b21a"/>
      </linearGradient>
      <linearGradient id="washYellow" x1="0" y1="0" x2="0" y2="1">
        <stop offset="0" stop-color="#f7b21a"/>
        <stop offset=".5" stop-color="#ffd21f"/>
        <stop offset="1" stop-color="#f29a1e"/>
      </linearGradient>
    </defs>
    <path d="M0 0 H450 C430 80 420 150 400 230 C380 330 300 380 150 420 C90 440 40 470 0 505 Z" fill="url(#washCool)"/>
    <path d="M30 568 C60 470 150 420 280 410 C380 400 430 420 520 420 C620 430 660 500 720 568 Z" fill="url(#washWarm)"/>
    <path d="M760 0 H880 C875 90 900 200 910 320 C920 420 905 500 920 568 H830 C840 470 860 380 840 300 C820 230 790 180 795 90 C800 50 780 20 760 0 Z" fill="url(#washYellow)"/>
    <path d="M1070 0 H1135 V470 C1110 440 1100 380 1095 300 C1090 200 1085 100 1070 0 Z" fill="#78cf2a"/>
  </svg>

  <div class="photo photo-boy" role="img" aria-label="Photo of a smiling boy jumping in a green striped polo shirt and denim shorts"></div>
  <div class="photo photo-girl" role="img" aria-label="Photo of a smiling girl with long dark hair in a white T-shirt and denim pinafore dress"></div>

  <div class="offer-lead">Take a<br><span class="indent">further</span></div>
  <div class="deal" aria-label="40% OFF">
    <span class="brace">{</span>
    <span class="amount">40%<br>OFF</span>
    <span class="brace">}</span>
  </div>
  <div class="offer-tail">all<br>stock</div>

  <div class="code-band">
    <span class="code">use code: TOVARELO</span>
    <span class="ends">Ends 31/12/2015</span>
  </div>

  <h1 class="headline">
    KICK BACK OR KICK IT
    <span class="line-two">UP A NOTCH THIS <span class="season">AUTUMN</span> IN</span>
  </h1>

  <div class="product-tag tag-polo">
    <span class="light">The most versatile</span>
    <span class="bold">Pique Striped Polo Shirts</span>
  </div>
  <div class="product-tag tag-dress">
    <span class="light">Pinafore Belt Strap</span>
    <span class="bold">Denim Dress</span>
  </div>
</main>
</body>
</html>
```